i need a business card for a plumbing company in california

we are a drain cleaning , maintenance plumbing company who is starting new marketing campaign for a tatrench-less pipe installation department .

the professional who appreciates time and quality workmanship.

Plumbing

0655a3
ec1f27

• the second logo needs to be included
• a focus on the services offered
• any underlined words on the brief

```html
<!DOCTYPE html>
<html lang="en">
<head>
<meta charset="utf-8">
<title>Clearline Plumbing – Business Card</title>
<link href="https://fonts.googleapis.com/css2?family=Montserrat:wght@500;600;700;800&display=swap" rel="stylesheet">
<style>
  :root{
    --blue:#0655a3;
    --red:#ec1f27;
    --red-dark:#b3121a;
    --charcoal:#2e2e30;
    --charcoal-dark:#1f1f21;
    --paper:#f3f2ee;
    --grey-text:#6d6d6d;
    --ink:#3a3a3a;
    --white:#ffffff;
    --stage:#e4e4e2;
  }
  *{box-sizing:border-box;margin:0;padding:0}
  html,body{width:1200px;height:972px;overflow:hidden}
  body{background:var(--stage);font-family:"Montserrat",sans-serif;position:relative}

  .card{position:absolute;width:587px;height:335px;overflow:hidden;box-shadow:0 4px 14px rgba(0,0,0,.25)}

  /* ---------- contact side ---------- */
  .card--contact{left:82px;top:194px;background:var(--paper)}
  .edge-blue{position:absolute;left:0;top:0;width:6px;height:100%;background:var(--blue)}
  .panel-dark{position:absolute;left:280px;top:0;width:285px;height:100%;background:var(--charcoal)}
  .edge-red{position:absolute;right:0;top:0;width:22px;height:100%;background:var(--red)}

  .brand-main{position:absolute;left:30px;top:58px;width:230px;text-align:center;
    color:var(--grey-text);font-weight:800;font-size:25px;line-height:26px}
  .services-list{position:absolute;left:30px;top:160px;width:212px;border-top:1px solid #9a9a9a;border-bottom:1px solid #9a9a9a;
    padding:13px 0 15px;text-align:center;font-size:9.5px;line-height:13.5px;color:var(--ink);font-weight:500;letter-spacing:.3px}
  .brand-badge{position:absolute;left:78px;top:256px;display:flex;align-items:center;gap:7px}
  .brand-badge .dot{width:26px;height:26px;border-radius:50%;background:var(--blue)}
  .brand-badge span{color:var(--blue);font-weight:800;font-size:17px}

  .ribbon-back{position:absolute;left:255px;top:104px}

  .person{position:absolute;left:293px;top:34px;color:var(--white)}
  .person__name{font-weight:800;font-size:20px;letter-spacing:.4px;text-transform:uppercase}
  .person__role{display:flex;align-items:center;gap:5px;font-size:11.5px;font-weight:600;letter-spacing:.6px;margin-top:4px}
  .person__role i{display:block;width:184px;height:1px;background:var(--white);margin-top:3px}

  .contacts{position:absolute;left:274px;top:129px;list-style:none}
  .contacts li{display:flex;align-items:center;height:25px;color:var(--white);font-size:11.5px;font-weight:600;letter-spacing:.3px}
  .contacts li.gap{margin-top:16px}
  .contacts .ico{width:18px;height:18px;border-radius:50%;background:var(--charcoal);display:flex;align-items:center;justify-content:center;margin-right:25px}

  /* ---------- promo side ---------- */
  .card--promo{left:344px;top:549px;background:var(--charcoal)}
  .promo-top{position:absolute;left:0;top:0;width:100%;height:162px;background:var(--paper)}
  .promo-brand{position:absolute;left:84px;top:48px;color:var(--grey-text);font-weight:800;font-size:22px;line-height:22px;text-align:center}
  .promo-badge{position:absolute;left:330px;top:48px;display:flex;align-items:center;gap:8px}
  .promo-badge .dot{width:30px;height:30px;border-radius:50%;background:var(--blue)}
  .promo-badge span{color:var(--blue);font-weight:800;font-size:19px}
  .ribbon-front{position:absolute;left:141px;top:138px}
  .tagline{position:absolute;left:172px;top:150px;width:244px;text-align:center;color:var(--white);
    font-weight:800;font-size:19px;letter-spacing:.5px;text-transform:uppercase}
  .offer{position:absolute;left:40px;top:224px;width:507px;text-align:center;color:var(--white);
    font-size:9.8px;line-height:17px;font-weight:600;letter-spacing:.3px;text-transform:uppercase}
  .offer strong{display:block;color:var(--red);font-size:15px;font-weight:800;line-height:20px;letter-spacing:.5px}
</style>
</head>
<body>

<section class="card card--contact" aria-label="Contact side">
  <div class="edge-blue"></div>
  <div class="panel-dark"></div>
  <div class="edge-red"></div>

  <div class="brand-main">Clearline<br>Plumbing</div>

  <p class="services-list">SEWER DRAIN CLEANING<br>- MAINTENANCE<br>- VIRGIN TRENCH-LESS INSTALLS</p>

  <div class="brand-badge"><div class="dot"></div><span>Clearline</span></div>

  <svg class="ribbon-back" width="50" height="200" viewBox="0 0 50 200">
    <polygon points="22,0 25,6 25,10 0,10" fill="var(--red-dark)"/>
    <polygon points="0,8 25,2 25,184 0,190" fill="var(--red)"/>
    <polygon points="25,2 48,8 48,180 25,184" fill="var(--red)"/>
    <polygon points="0,190 25,184 25,192" fill="var(--red-dark)"/>
    <polygon points="48,96 42,100 48,104" fill="var(--charcoal-dark)"/>
  </svg>

  <div class="person">
    <h1 class="person__name">Marco Estrada Jr</h1>
    <p class="person__role">OWNER <i></i></p>
  </div>

  <ul class="contacts">
    <li><span class="ico"><svg width="10" height="10" viewBox="0 0 10 10"><path d="M2 1 L3.6 1 L4.2 3 L3.2 3.8 Q4 5.8 6.2 6.8 L7 5.8 L9 6.4 L9 8 Q8.5 9 7.5 9 Q1 8 1 2.5 Q1 1 2 1Z" fill="#fff"/></svg></span>(555) 014-2286</li>
    <li><span class="ico"><svg width="10" height="8" viewBox="0 0 10 8"><rect x="0.5" y="0.5" width="9" height="7" fill="#fff"/><path d="M0.5 0.8 L5 4.5 L9.5 0.8" stroke="var(--charcoal)" fill="none"/></svg></span>info@ClearlinePlumbing.com</li>
    <li><span class="ico"><svg width="10" height="10" viewBox="0 0 10 10"><circle cx="5" cy="5" r="4.5" fill="#fff"/><ellipse cx="5" cy="5" rx="2" ry="4.5" stroke="var(--charcoal)" fill="none" stroke-width=".8"/><line x1=".5" y1="5" x2="9.5" y2="5" stroke="var(--charcoal)" stroke-width=".8"/></svg></span>www.ClearlinePlumbing.com</li>
    <li class="gap"><span class="ico"></span>Facebook@ClearlinePlumbing</li>
    <li><span class="ico"></span>ClearlinePlumbingCo</li>
  </ul>
</section>

<section class="card card--promo" aria-label="Promotional side">
  <div class="promo-top"></div>
  <div class="promo-brand">Clearline<br>Plumbing</div>
  <div class="promo-badge"><div class="dot"></div><span>Clearline</span></div>

  <svg class="ribbon-front" width="305" height="52" viewBox="0 0 305 52">
    <polygon points="8,0 14,0 14,24 0,24" fill="var(--red-dark)"/>
    <polygon points="291,0 297,0 305,24 291,24" fill="var(--red-dark)"/>
    <polygon points="12,0 293,0 285,48 20,48" fill="var(--red)"/>
  </svg>
  <p class="tagline">Lead by example..</p>

  <p class="offer">Virgin trench-less installs &amp; replacements - pipe bursting &amp; pipe<br>piercing install, replace, pipe enlargement<strong>PULL &amp; GO</strong></p>
</section>

</body>
</html>
```